business card for a shoe shop

we would like a business card for a family owned shoe shop.
With this information included.
Darnell's Shoe Store
Family owned since 1947

then on other side
Darnell's Shoe Store
Footwear fitting specialist
Phone: 9187 2630
218 Quarry St, Fernleigh Downs 3187
(cnr. Hartwick Rd and Quarry St)
darnellshoes218@examplemail.com
if could incorporate the purple color on card i have attached.

```html
<!DOCTYPE html>
<html lang="en">
<head>
<meta charset="utf-8">
<title>Darnell's Shoe Store – Business Card</title>
<link rel="stylesheet" href="https://fonts.googleapis.com/css2?family=Lato:wght@700;900&family=Open+Sans:wght@300;400&family=Poppins:wght@300;400&display=swap">
<style>
  :root {
    --page-bg: #efefef;
    --card-frame: #984dff;
    --card-face: #ffffff;
    --ink-purple: #8a4af0;
  }
  * { margin: 0; padding: 0; box-sizing: border-box; }
  html, body {
    width: 1200px;
    height: 958px;
    overflow: hidden;
    background: var(--page-bg);
  }
  .canvas {
    position: relative;
    width: 1200px;
    height: 958px;
  }
  .card {
    position: absolute;
    left: 328px;
    width: 553px;
    height: 331px;
    background: var(--card-frame);
    border-radius: 22px;
    padding: 18px 23px 17px 23px;
  }
  .card--front { top: 126px; }
  .card--back  { top: 523px; }
  .card__face {
    position: relative;
    width: 100%;
    height: 100%;
    background: var(--card-face);
    border-radius: 15px;
    color: var(--ink-purple);
    text-align: center;
  }
  .front__name {
    position: absolute;
    left: 0; right: 0;
    top: 111px;
    font-family: "Lato", sans-serif;
    font-weight: 900;
    font-size: 38px;
    letter-spacing: -1.2px;
    line-height: 1;
    text-transform: uppercase;
  }
  .front__tagline {
    position: absolute;
    left: 0; right: 0;
    top: 166px;
    font-family: "Lato", sans-serif;
    font-weight: 700;
    font-size: 14px;
    letter-spacing: -0.4px;
    line-height: 1;
    text-transform: uppercase;
  }
  .back__name {
    position: absolute;
    left: 0; right: 0;
    top: 28px;
    font-family: "Poppins", sans-serif;
    font-weight: 400;
    font-size: 34px;
    line-height: 1.3;
  }
  .back__specialty {
    position: absolute;
    left: 0; right: 0;
    top: 86px;
    font-family: "Open Sans", sans-serif;
    font-weight: 400;
    font-size: 22px;
    line-height: 1.3;
  }
  .back__contact {
    position: absolute;
    left: 0; right: 0;
    top: 146px;
    font-family: "Poppins", sans-serif;
    font-weight: 300;
    font-size: 18px;
    line-height: 27px;
    letter-spacing: 0.6px;
    font-style: normal;
  }
</style>
</head>
<body>
  <main class="canvas">
    <section class="card card--front">
      <div class="card__face">
        <h1 class="front__name">Darnell's Shoe Store</h1>
        <p class="front__tagline">Family owned since 1947</p>
      </div>
    </section>

    <section class="card card--back">
      <div class="card__face">
        <h2 class="back__name">Darnell's Shoe Store</h2>
        <p class="back__specialty">Footwear fitting specialist</p>
        <address class="back__contact">
          <div class="contact__phone">Phone: 9187 2630</div>
          <div class="contact__street">218 Quarry St, Fernleigh Downs 3187</div>
          <div class="contact__corner">(cnr. Hartwick Rd and Quarry St)</div>
          <div class="contact__email">darnellshoes218@examplemail.com</div>
        </address>
      </div>
    </section>
  </main>
</body>
</html>
```